TomasTunes poster

We need a poster to promote my live music show for hotels, Im playing for tourists in hotels in Palma de Mallorca, Spain, I would like to see the url of my web site in the poster www.tomastunes.es, in the web site you can see some of my music, thx

```html
<!DOCTYPE html>
<html lang="en">
<head>
<meta charset="utf-8">
<title>TomasTunes – Live Music Poster</title>
<link rel="stylesheet" href="https://fonts.googleapis.com/css2?family=Black+Ops+One&family=Oswald:wght@500;600&family=Architects+Daughter&family=Kurale&display=swap">
<style>
  :root {
    --paper: #ffffff;
    --night: #000000;
    --ink-white: #ffffff;
    --sun-yellow: #f2e52a;
    --paint-blue: #1f9be2;
    --paint-green: #2ec55b;
    --paint-yellow: #f6e61c;
    --paint-magenta: #e03fe0;
    --paint-orange: #f7941d;
    --photo-light: #b9b9b9;
    --photo-mid: #7a7a7a;
    --photo-dark: #2b2b2b;
  }
  * { margin: 0; padding: 0; box-sizing: border-box; }
  html, body {
    width: 867px; height: 1200px; overflow: hidden;
    background: var(--paper);
  }
  .poster {
    position: relative;
    width: 867px; height: 1200px;
    background: var(--paper);
  }
  .poster-panel {
    position: absolute;
    left: 26px; top: 25px; width: 815px; height: 1150px;
    background: var(--night);
    overflow: hidden;
  }
  .brand-name {
    position: absolute;
    top: 105px; left: 0; width: 100%;
    text-align: center;
    font-family: "Oswald", sans-serif;
    font-weight: 600;
    font-size: 58px;
    letter-spacing: 2px;
    color: var(--ink-white);
  }
  .headline {
    position: absolute;
    top: 318px; left: 0; width: 100%;
    text-align: center;
    font-family: "Black Ops One", sans-serif;
    font-size: 152px;
    line-height: 1;
    letter-spacing: 14px;
  }
  .headline .m { color: var(--paint-blue); }
  .headline .u { color: var(--paint-green); }
  .headline .s { color: var(--paint-yellow); }
  .headline .i { color: var(--paint-magenta); }
  .headline .c { color: var(--paint-orange); }

  .performance-photo {
    position: absolute;
    left: 14px; top: 470px; width: 787px; height: 560px;
    background:
      radial-gradient(ellipse 55% 50% at 50% 50%, var(--photo-mid) 0%, rgba(120,120,120,0.6) 60%, rgba(0,0,0,0) 100%),
      linear-gradient(180deg, rgba(0,0,0,1) 0%, rgba(60,60,60,0.9) 18%, var(--photo-mid) 45%, var(--photo-light) 82%, rgba(40,40,40,0.8) 100%);
    filter: blur(4px);
  }
  .event-details {
    position: absolute;
    top: 893px; left: 0; width: 100%;
    display: flex; justify-content: center; align-items: center;
    font-family: "Architects Daughter", cursive;
    color: var(--sun-yellow);
    text-transform: none;
  }
  .save-date { text-align: center; padding-right: 12px; line-height: 1; }
  .save-date .big { font-size: 38px; display: block; }
  .save-date .small { font-size: 23px; display: block; margin-top: 4px; }
  .divider { width: 2px; height: 86px; background: var(--sun-yellow); }
  .event-day { padding: 0 6px 0 14px; font-size: 37px; line-height: 1.1; }
  .event-year {
    font-size: 40px; line-height: 1;
    writing-mode: vertical-rl; transform: rotate(180deg);
    padding-right: 8px;
  }
  .event-time { padding-left: 14px; font-size: 37px; line-height: 1.1; }

  .venue {
    position: absolute;
    top: 1014px; left: 0; width: 100%;
    display: flex; justify-content: center; align-items: center; gap: 10px;
    font-family: "Oswald", sans-serif;
    font-weight: 600;
    font-size: 23px;
    color: var(--ink-white);
    letter-spacing: 0.3px;
  }
  .contact-bar {
    position: absolute;
    top: 1062px; left: 0; width: 100%;
    display: flex; justify-content: center; align-items: center; gap: 22px;
    font-family: "Kurale", serif;
    font-size: 22px;
    color: var(--ink-white);
  }
  .contact-item { display: flex; align-items: center; gap: 6px; }
  .contact-item.phone { font-size: 27px; }
  .icon { width: 18px; height: 18px; stroke: var(--ink-white); fill: none; stroke-width: 1.5; }
</style>
</head>
<body>
<main class="poster">
  <section class="poster-panel">
    <h1 class="brand-name">TomasTunes</h1>

    <h2 class="headline" aria-label="Music">
      <span class="m">M</span><span class="u">U</span><span class="s">S</span><span class="i">I</span><span class="c">C</span>
    </h2>

    <div class="performance-photo" role="img" aria-label="Black and white photo of a guitarist seated on a hotel terrace above a harbour, with an amplifier and microphone stand"></div>

    <div class="event-details">
      <div class="save-date"><span class="big">SAVE</span><span class="small">THE DATE</span></div>
      <div class="divider"></div>
      <div class="event-day">SUNDAY<br>2nd JULY</div>
      <div class="event-year">2019</div>
      <div class="divider"></div>
      <div class="event-time">5pm to<br>10pm</div>
    </div>

    <p class="venue">
      <svg class="icon" viewBox="0 0 20 20" aria-hidden="true"><path d="M10 18s-6-6.5-6-10.5a6 6 0 0 1 12 0C16 11.5 10 18 10 18z"/><circle cx="10" cy="7.5" r="2"/></svg>
      #5120, HARBOUR AVENUE PARK NEXT MARINA TOWER SPAIN
    </p>

    <footer class="contact-bar">
      <span class="contact-item">
        <svg class="icon" viewBox="0 0 20 20" aria-hidden="true"><circle cx="10" cy="10" r="8"/><ellipse cx="10" cy="10" rx="3.5" ry="8"/><path d="M2 10h16M3.5 6h13M3.5 14h13"/></svg>
        www.tomastunes.es
      </span>
      <span class="contact-item">
        <svg class="icon" viewBox="0 0 20 20" aria-hidden="true"><rect x="2" y="4.5" width="16" height="11"/><path d="M2 4.5l8 6.5 8-6.5"/></svg>
        songs@ www.tomastunes.es
      </span>
      <span class="contact-item phone">
        <svg class="icon" viewBox="0 0 20 20" aria-hidden="true"><path d="M3 8c0-2 3-4 7-4s7 2 7 4l-3 1-1-2H7L6 9z"/><rect x="5" y="10" width="10" height="6" rx="1"/></svg>
        0987654321
      </span>
    </footer>
  </section>
</main>
</body>
</html>
```